Design a single page Shopify store web page

We are looking to have a page designed for a single page Shopify store with 2 products. We already have a basic structure that we like, though we are open to suggestions. We are looking for somebody to provide a design/color scheme that we can then implement using Shopify's templating system. We can handle the implementation(HTML / CSS / jS) as we already have 2 web developers on the team, but have not been able to find a design we liked.

The job would consist of providing a mockup (photoshop or otherwise) and any vector graphics you choose to create for the site (we can provide product photos and other images).

You can also look at http://brickwellgoods.com.au for some of our design direction we have used so far

Target Market(s)

Young Australian Males (18 - 49)

Industry/Entity Type

Store

Number of Pages Required

1 page

Font styles to use
Serif
Sans Serif

Requirements
Must have
• Single Page Design
• E-commerce Product Purchase
• Manly (whatever interpretation of that you have)

```html
<!DOCTYPE html>
<html lang="en">
<head>
<meta charset="utf-8">
<title>Brickwell Goods – Underwear &amp; Sock Plans</title>
<link href="https://fonts.googleapis.com/css2?family=Open+Sans:wght@400;600;700;800&display=swap" rel="stylesheet">
<style>
  :root{
    --blue:#12a6e8;
    --blue-dark:#0b8fcc;
    --black:#151515;
    --ink:#333;
    --muted:#777;
    --panel:#f0f0f0;
    --white:#fff;
    --line:#dedede;
  }
  *{box-sizing:border-box;margin:0;padding:0}
  html,body{width:688px;height:1200px;overflow:hidden}
  body{font-family:"Open Sans",Arial,sans-serif;color:var(--ink);background:var(--white);position:relative}

  /* header */
  .site-header{height:46px;background:var(--black);display:flex;align-items:center;justify-content:space-between;padding:0 48px 0 100px}
  .brand{color:var(--white);font-weight:600;font-size:15px;letter-spacing:.3px}
  .nav{display:flex;gap:18px;align-items:center}
  .nav a{color:#ddd;font-size:8px;text-decoration:none;font-weight:600}
  .nav .nav-cta{border:1px solid var(--blue);color:var(--white);padding:4px 8px;border-radius:2px}

  /* hero */
  .hero{position:relative;height:274px;background:var(--blue);overflow:hidden}
  .hero-photo,.hero-stripe{position:absolute;top:0;left:262px;width:426px;height:274px}
  .hero-photo{clip-path:polygon(54% 0,100% 0,100% 100%,3% 100%);background:linear-gradient(135deg,#2d3e55 0%,#c9c3b8 45%,#e07a3f 65%,#2b5aa5 85%,#b79a74 100%)}
  .hero-stripe{clip-path:polygon(51% 0,53% 0,2% 100%,0 100%);background:var(--white)}
  .hero-copy{position:absolute;left:100px;top:56px;color:var(--white)}
  .hero-copy h1{font-size:25px;font-weight:800;letter-spacing:1px;margin-bottom:12px}
  .hero-copy p{font-size:14px;font-weight:800;line-height:26px;text-transform:uppercase}
  .hero-copy p .dark{color:var(--black)}
  .hero-arrows{position:absolute;left:100px;top:230px;display:flex;gap:6px}

  /* how it works */
  .how{background:var(--panel);height:185px;padding-top:16px}
  .section-title{text-align:center;font-size:15px;font-weight:700;color:var(--ink)}
  .steps{display:flex;justify-content:center;gap:22px;margin-top:14px}
  .step{width:142px;height:120px;background:var(--white);border:1px solid var(--line);text-align:center;padding:10px 12px}
  .step h3{font-size:10px;font-weight:600;margin-bottom:8px}
  .step p{font-size:6.5px;line-height:9px;color:var(--muted);margin-top:8px}
  .step-icon{width:38px;height:38px;border-radius:50%;margin:0 auto;display:flex;align-items:center;justify-content:center}
  .step .step-icon{background:var(--blue)}
  .step.is-active{background:var(--blue);border-color:var(--blue);color:var(--white)}
  .step.is-active p{color:#e8f6fd}
  .step.is-active .step-icon{background:var(--white)}

  /* plans */
  .plans{background:var(--blue);height:280px;padding-top:16px}
  .plans .section-title{color:var(--white)}
  .plan-row{display:flex;justify-content:center;gap:34px;margin-top:14px}
  .plan{width:202px;height:178px;background:var(--white);border-radius:3px;padding:8px}
  .plan-head{display:flex;justify-content:space-between;align-items:center;font-size:10px;font-weight:700;margin-bottom:8px}
  .plan-head .price{margin-left:auto;margin-right:8px}
  .join{background:var(--blue);color:var(--white);font-size:6.5px;padding:2px 8px;border-radius:2px}
  .plan-media{display:flex;gap:6px;height:140px}
  .media-main{flex:0 0 110px;height:118px}
  .media-side{display:flex;flex-direction:column;gap:4px;flex:1}
  .media-side div{height:57px}
  .photo-a{background:linear-gradient(160deg,#c9b7a4,#6f5c4c)}
  .photo-b{background:linear-gradient(160deg,#e9e4df,#b39a86)}
  .photo-c{background:linear-gradient(160deg,#3b3b40,#9a8f86)}
  .perks{display:flex;justify-content:center;gap:32px;margin-top:14px}
  .perk{display:flex;align-items:center;gap:5px;color:var(--white);font-size:8px;font-weight:600}

  /* faq */
  .faq{height:355px;padding:14px 100px 0}
  .faq .section-title{margin-bottom:12px}
  .faq-item{border:1px solid var(--line);height:22px;display:flex;align-items:center;justify-content:space-between;padding:0 8px;font-size:8px;font-weight:600;margin-bottom:9px}
  .faq-item.is-open{background:var(--blue);border-color:var(--blue);color:var(--white);margin-bottom:0}
  .faq-toggle{width:11px;height:11px;border-radius:50%;background:#555;color:var(--white);font-size:9px;line-height:11px;text-align:center;font-weight:700}
  .is-open .faq-toggle{background:var(--white);color:var(--blue)}
  .faq-answer{border:1px solid var(--line);border-top:none;padding:10px 8px;font-size:6.5px;line-height:10px;color:var(--muted);height:102px;margin-bottom:14px}

  /* footer */
  .site-footer{position:absolute;left:0;bottom:0;width:688px;height:60px;background:var(--black);padding:10px 100px;color:#aaa;font-size:6.5px}
  .footer-row{display:flex;justify-content:space-between;align-items:center}
  .footer-links a{color:#aaa;text-decoration:none}
  .social{display:flex;gap:4px;margin-top:8px}
  .social span{width:11px;height:11px;background:#444}
  .pay{display:flex;gap:4px;margin-top:8px;justify-content:flex-end}
  .pay span{width:20px;height:12px;border-radius:2px;background:#ddd}
</style>
</head>
<body>

<header class="site-header">
  <div class="brand">Brickwell Goods</div>
  <nav class="nav">
    <a href="#how">How It Works</a>
    <a href="#plans">Plans</a>
    <a href="#faq">FAQ</a>
    <a href="#about">About Us</a>
    <a href="#signup" class="nav-cta">Sign Up Now!</a>
  </nav>
</header>

<section class="hero">
  <div class="hero-photo" role="img" aria-label="Legs in jeans wearing colourful patterned socks on a wooden floor"></div>
  <div class="hero-stripe"></div>
  <div class="hero-copy">
    <h1>AUTOMATE YOUR LIFE</h1>
    <p>New underwear <span class="dark">and</span> sock</p>
    <p>Delivers to your door</p>
    <p>When you <span class="dark">need it</span></p>
  </div>
  <div class="hero-arrows">
    <svg width="12" height="8" viewBox="0 0 12 8"><path d="M11 4H2M5 1L2 4l3 3" stroke="#fff" stroke-width="1.5" fill="none"/></svg>
    <svg width="12" height="8" viewBox="0 0 12 8"><path d="M1 4h9M7 1l3 3-3 3" stroke="#fff" stroke-width="1.5" fill="none"/></svg>
  </div>
</section>

<section class="how" id="how">
  <h2 class="section-title">How It Works?</h2>
  <div class="steps">
    <div class="step">
      <h3>1.Choose a Plan</h3>
      <div class="step-icon"><svg width="20" height="20" viewBox="0 0 20 20"><rect x="3" y="3" width="14" height="14" rx="2" fill="none" stroke="#fff" stroke-width="1.6"/><path d="M6 10l3 3 5-6" stroke="#fff" stroke-width="1.8" fill="none"/></svg></div>
      <p>Pick one of our plans to suit all budgets and styles.</p>
    </div>
    <div class="step is-active">
      <h3>2.Choose How Often</h3>
      <div class="step-icon"><svg width="20" height="20" viewBox="0 0 20 20"><path d="M4 5h12M4 10h12M4 15h12" stroke="#12a6e8" stroke-width="2"/></svg></div>
      <p>Decide whether you would like to receive new underwear every 3 or 6 months.</p>
    </div>
    <div class="step">
      <h3>3.Get Your Pack</h3>
      <div class="step-icon"><svg width="20" height="20" viewBox="0 0 20 20"><path d="M5 7h10l-1 10H6z" fill="none" stroke="#fff" stroke-width="1.6"/><path d="M7.5 7a2.5 2.5 0 015 0" fill="none" stroke="#fff" stroke-width="1.6"/></svg></div>
      <p>We'll send you your first pack right away and then again every 3 or 6 months.</p>
    </div>
  </div>
</section>

<section class="plans" id="plans">
  <h2 class="section-title">Plans</h2>
  <div class="plan-row">
    <article class="plan">
      <div class="plan-head"><span>Comfort</span><span class="price">$ 30</span><span class="join">Join</span></div>
      <div class="plan-media">
        <div class="media-main photo-a" role="img" aria-label="Models wearing the Comfort underwear range"></div>
        <div class="media-side">
          <div class="photo-c" role="img" aria-label="Comfort trunks close-up"></div>
          <div class="photo-b" role="img" aria-label="Comfort trunks folded"></div>
        </div>
      </div>
    </article>
    <article class="plan">
      <div class="plan-head"><span>Style</span><span class="price">$ 30</span><span class="join">Join</span></div>
      <div class="plan-media">
        <div class="media-main photo-b" role="img" aria-label="Model wearing the Style briefs"></div>
        <div class="media-side">
          <div class="photo-a" role="img" aria-label="Style briefs close-up"></div>
          <div class="photo-c" role="img" aria-label="Style briefs alternate colour"></div>
        </div>
      </div>
    </article>
  </div>
  <div class="perks">
    <div class="perk"><svg width="10" height="10" viewBox="0 0 10 10"><path d="M1 5l3 3 5-6" stroke="#7ee04a" stroke-width="2" fill="none"/></svg>Free Shipping</div>
    <div class="perk"><svg width="10" height="10" viewBox="0 0 10 10"><path d="M1 5l3 3 5-6" stroke="#7ee04a" stroke-width="2" fill="none"/></svg>Easy Returns</div>
    <div class="perk"><svg width="10" height="10" viewBox="0 0 10 10"><path d="M1 5l3 3 5-6" stroke="#7ee04a" stroke-width="2" fill="none"/></svg>Cancel Whenever</div>
    <div class="perk"><svg width="10" height="10" viewBox="0 0 10 10"><path d="M1 5l3 3 5-6" stroke="#7ee04a" stroke-width="2" fill="none"/></svg>Satisfaction Guaranteed</div>
  </div>
</section>

<section class="faq" id="faq">
  <h2 class="section-title">FAQ</h2>
  <div class="faq-item is-open"><span>What is Brickwell Goods?</span><span class="faq-toggle">−</span></div>
  <div class="faq-answer">Brickwell Goods is a simple subscription for the essentials every man needs. Choose a plan, pick how often you want a fresh pack, and we deliver quality underwear and socks straight to your door. No more shopping trips, no more worn out basics. Change or cancel your plan at any time from your account, with free shipping on every order across Australia.</div>
  <div class="faq-item"><span>What is your Satisfaction Guarantee?</span><span class="faq-toggle">+</span></div>
  <div class="faq-item"><span>Shipping Policy</span><span class="faq-toggle">+</span></div>
  <div class="faq-item"><span>What do I get with my Plan?</span><span class="faq-toggle">+</span></div>
  <div class="faq-item"><span>Return Policy</span><span class="faq-toggle">+</span></div>
</section>

<footer class="site-footer">
  <div class="footer-row">
    <div>
      <div class="footer-links"><a href="#">Shipping</a> | <a href="#">Returns</a> | <a href="#">Payment</a> | <a href="#">Terms</a> | <a href="#">Privacy</a> &nbsp;&nbsp; Email Us : hello@brickwellgoods.com.au</div>
      <div class="social"><span></span><span></span><span></span></div>
    </div>
    <div>
      <div>Copyright 2024 Brickwell Goods. All Rights Reserved.</div>
      <div class="pay"><span></span><span></span><span></span><span></span></div>
    </div>
  </div>
</footer>

</body>
</html>
```